Business card design needed

I am a local business in the Blue Mountains area of Sydney. I am a sole trader and the business has been operating 7 months. To date the business has been built on referrals only and all my clinets for both home & commercial services are themselves business owners. I specialise in Home and Office cleaning and small business cleaning for example cafes, restuarants, health clinics.
I would like a clean looking design( maybe a white background). If its possible(not madatory) to incorporate a duster, or mop & bucket into the design or roof tops to communicate business premises that would be great. I would like my clients to know what the business is from the card. My uniform is navy with red/pink logo on .Attatched is the unifrom logo but it is not critical to match the font for the business card.
please put my name on contact details; Carol Whitby, Business owner.
Updates
Thank you very much to all the designers and their work efforts to submit a design for Bright Feather Domestic Services. I have made a decision to accept the deign that Velo Design of the United States submitted. Again Many thanks. Carol
Target Market(s)
business owners, generally women between 35-55
Industry/Entity Type
Small Business
Contact Information for Business Card
Bright Feather Domestic Services,
specialist in Home & Small business cleaning
Lithgow NSW
tel: 0491570156 0491tidyup
Logo Text
Bright Feather Domestic Servies
Logo styles of interest
Emblem Logo
Abstract Logo
Wordmark Logo
Look and feel

```html
<!DOCTYPE html>
<html lang="en">
<head>
<meta charset="utf-8">
<title>Bright Feather Domestic Services – Business Card</title>
<link href="https://fonts.googleapis.com/css2?family=Open+Sans:wght@400;600;700&display=swap" rel="stylesheet">
<style>
  :root{
    --navy:#0b2f7a;
    --blue:#1b6fb0;
    --red:#f0161a;
    --card:#f4f5f7;
    --paper:#ffffff;
    --stage:#e6e7ea;
    --ink-soft:#9aa6b8;
    --outline:#1c2a4a;
  }
  *{margin:0;padding:0;box-sizing:border-box}
  html,body{width:1200px;height:1000px;overflow:hidden}
  body{background:var(--stage);font-family:"Open Sans",Arial,sans-serif;position:relative}
  .card{position:absolute;left:220px;width:760px;height:434px;background:linear-gradient(160deg,var(--paper),var(--card));box-shadow:0 6px 18px rgba(0,0,0,.18);overflow:hidden}
  .card--front{top:44px}
  .card--back{top:522px}
  .card__art{position:absolute;inset:0}
  .brand-mark{position:absolute;left:300px;top:150px;display:flex;align-items:center;gap:14px}
  .brand-mark__dot{width:22px;height:22px;border-radius:50%;background:var(--paper)}
  .brand-mark__name{color:var(--paper);font-size:40px;font-weight:600;letter-spacing:.5px}
  .front__title{position:absolute;right:34px;top:356px;color:var(--navy);font-size:26px;font-weight:400}
  .back__watermark{position:absolute;left:120px;top:300px;font-size:64px;font-weight:600;color:var(--ink-soft);opacity:.12;transform:rotate(-14deg)}
  .contact{position:absolute;right:38px;top:160px;text-align:right;color:var(--navy)}
  .contact__company{font-size:25px;font-weight:400;line-height:1.1}
  .contact__tagline{font-size:15px;font-weight:400;margin-top:2px}
  .contact__person{font-size:21px;font-weight:700;color:var(--paper);margin-top:14px;
    text-shadow:1px 1px 0 var(--outline),-1px -1px 0 var(--outline),1px -1px 0 var(--outline),-1px 1px 0 var(--outline),2px 2px 3px rgba(0,0,0,.45)}
  .contact__line{display:flex;justify-content:flex-end;align-items:center;gap:12px;margin-top:10px;font-size:15px}
  .contact__line--phone{font-size:23px;font-weight:700;color:var(--paper);
    text-shadow:1px 1px 0 var(--outline),-1px -1px 0 var(--outline),1px -1px 0 var(--outline),-1px 1px 0 var(--outline),2px 2px 3px rgba(0,0,0,.45)}
  .contact__icon{width:34px;height:26px;flex:none}
</style>
</head>
<body>

<section class="card card--front" aria-label="Card front">
  <svg class="card__art" viewBox="0 0 760 434" aria-hidden="true">
    <defs>
      <linearGradient id="band" x1="0" y1="1" x2="1" y2="0">
        <stop offset="0" stop-color="#0b2f7a"/>
        <stop offset="1" stop-color="#1b6fb0"/>
      </linearGradient>
    </defs>
    <path d="M0,434 L0,400 C150,230 330,60 520,0 L760,0 L760,110 C560,170 300,260 110,434 Z" fill="url(#band)"/>
    <path d="M110,434 C300,260 560,170 760,110 L760,152 C580,212 330,300 172,434 Z" fill="#f0161a"/>
  </svg>
  <div class="brand-mark">
    <span class="brand-mark__dot"></span>
    <span class="brand-mark__name">Bright Feather</span>
  </div>
  <p class="front__title">Bright Feather Domestic Services</p>
</section>

<section class="card card--back" aria-label="Card back">
  <svg class="card__art" viewBox="0 0 760 434" aria-hidden="true">
    <defs>
      <linearGradient id="corner" x1="0" y1="0" x2="1" y2="0">
        <stop offset="0" stop-color="#1b6fb0"/>
        <stop offset="1" stop-color="#0b2f7a"/>
      </linearGradient>
    </defs>
    <path d="M0,0 L445,0 C400,110 170,190 0,380 Z" fill="url(#corner)"/>
  </svg>
  <span class="back__watermark" aria-hidden="true">Bright Feather</span>
  <div class="contact">
    <p class="contact__company">Bright Feather Domestic Services</p>
    <p class="contact__tagline">specialist in Home &amp; Small business cleaning</p>
    <p class="contact__person">Carol Whitby, Business owner</p>
    <p class="contact__line contact__line--phone">
      <svg class="contact__icon" viewBox="0 0 34 26" aria-hidden="true">
        <path d="M3,9 C3,3 31,3 31,9 L31,11 L24,11 L24,8 L10,8 L10,11 L3,11 Z" fill="#0b2f7a"/>
        <path d="M9,12 L25,12 L30,24 L4,24 Z" fill="#0b2f7a"/>
        <circle cx="17" cy="18" r="3.5" fill="#f4f5f7"/>
      </svg>
      0491570156
    </p>
    <p class="contact__line">
      <svg class="contact__icon" viewBox="0 0 34 26" aria-hidden="true">
        <rect x="2" y="4" width="30" height="18" fill="#0b2f7a"/>
        <path d="M2,4 L17,15 L32,4" fill="none" stroke="#f4f5f7" stroke-width="2"/>
      </svg>
      brightfeather@tidymail.com
    </p>
    <p class="contact__line">
      <svg class="contact__icon" viewBox="0 0 34 26" aria-hidden="true">
        <g fill="none" stroke="#0b2f7a" stroke-width="2">
          <circle cx="17" cy="13" r="11"/>
          <ellipse cx="17" cy="13" rx="5" ry="11"/>
          <path d="M6,13 H28 M8,7 H26 M8,19 H26"/>
        </g>
      </svg>
      www.brightfeather.com.au
    </p>
  </div>
</section>

</body>
</html>
```